Label design: italian artisan honey (to allow tradition look attractive!)

Founded in 1973, this specialized business in artisan honey, is based in Emilia-Romagna. It accounts for 10 apiary locations, honey is organic, whereas the equipment to rise, and control bees are all hand made.
The symbol, (you will find the logo corvasti.ai) is a hexagonal hunting house built in the 17th century. The structure is protected by fine-arts and retains its stucco works and frescoes depicting mythological scenes. The place is located in the hills, next to a hunting area, and surrounded by our ecological farm.

Please find the foto of the label that has been used for over 30 years and also the Italian Beekeeper association label that is placed on all the vases.

Target Market(s)

Local gastronomic shop owners, where local consumers are both young and mature families, well-read, connaisseurs, curious, with strong social ties also with nature.

Font styles to use
Serif
Sans Serif

Requirements
Must have
• We have a glass jar already with specific dimensions.
The lid finishing is metallic finishing, in copper color.
We need the label to have the by-law necessary information of the product on it:
Honey type, producer name, weight, best by date, origin.
The lid measures 6 cm in diameter, and has a border of about 0.5 cm.
The visible part of the glass jar is 3 cm high.
You can get inspired by the type of package we want to use: (in light wood or carton board as materials as in the 2 examples we attach is actually like a matchbox).
We also attached an illustrator file with the logo shape, colors to be adapted to your design, consider the "grey color" and the "metallic finishing" on the corner, as shown in the file ref_glimboard_3.
Nice to have
• The _pack_1 and _pack_3 files are mood ideas for the box, to provide you inspiration for the label.
The color palette is provided by two files :
ref_glimboard_3 ;
color_palette_corvasti.
The font reference is provided by two files :
Typeface ;
ref_typeface.

```html
<!DOCTYPE html>
<html lang="it">
<head>
<meta charset="utf-8">
<title>Corvasti – Etichetta Miele</title>
<link rel="stylesheet" href="https://fonts.googleapis.com/css2?family=Josefin+Sans:wght@300;600;700&display=swap">
<style>
  :root {
    --backdrop: #b97429;
    --label-green: #3f524d;
    --band-stone: #a8a38c;
    --band-stone-light: #b1ac95;
    --band-stone-dark: #a09a82;
    --gold-dark: #8a5a1e;
    --gold-light: #e9c57c;
    --flag-green: #3d8a46;
    --flag-white: #f2f0ea;
    --flag-red: #d9532c;
  }
  html, body {
    margin: 0;
    padding: 0;
    width: 819px;
    height: 1200px;
    overflow: hidden;
    background: var(--backdrop);
  }
  .label-sheet {
    display: block;
    width: 819px;
    height: 1200px;
  }
  .brand-name {
    font-family: "Josefin Sans", sans-serif;
    font-weight: 300;
    letter-spacing: 2px;
  }
  .product-name {
    font-family: "Josefin Sans", sans-serif;
    font-weight: 700;
  }
  .origin-text {
    font-family: "Josefin Sans", sans-serif;
    font-weight: 700;
    letter-spacing: 1px;
  }
  .legal-text {
    font-family: "Josefin Sans", sans-serif;
    font-weight: 600;
    letter-spacing: 1px;
  }
</style>
</head>
<body>
<svg class="label-sheet" viewBox="50 546 1486 2177" xmlns="http://www.w3.org/2000/svg">
  <defs>
    <linearGradient id="gold" x1="0" y1="0" x2="1" y2="1">
      <stop offset="0" stop-color="var(--gold-dark)"/>
      <stop offset="0.5" stop-color="var(--gold-light)"/>
      <stop offset="1" stop-color="#a8742a"/>
    </linearGradient>
    <linearGradient id="band-fill" x1="0" y1="0" x2="1" y2="1">
      <stop offset="0" stop-color="var(--band-stone-light)"/>
      <stop offset="0.5" stop-color="var(--band-stone)"/>
      <stop offset="1" stop-color="var(--band-stone-dark)"/>
    </linearGradient>
    <radialGradient id="scroll-glow" cx="0.5" cy="0.5" r="0.5">
      <stop offset="0" stop-color="#d6ad62" stop-opacity="0.45"/>
      <stop offset="1" stop-color="#d6ad62" stop-opacity="0"/>
    </radialGradient>
    <filter id="soft-shadow" x="-10%" y="-10%" width="120%" height="120%">
      <feDropShadow dx="0" dy="6" stdDeviation="10" flood-color="#5a3510" flood-opacity="0.35"/>
    </filter>
  </defs>

  <!-- body band -->
  <g class="body-band">
    <rect x="85" y="1975" width="1415" height="235" fill="url(#band-fill)"
          role="img" aria-label="Motivo floreale a linee sottili su fondo pietra"/>
    <ellipse class="scroll-area" cx="612" cy="2138" rx="78" ry="48" fill="url(#scroll-glow)"
             role="img" aria-label="Volute dorate decorative"/>
    <ellipse class="scroll-area" cx="974" cy="2138" rx="78" ry="48" fill="url(#scroll-glow)"
             role="img" aria-label="Volute dorate decorative"/>

    <g class="legal-info" fill="var(--label-green)">
      <text class="legal-text" x="340" y="2078" text-anchor="middle" font-size="30">PESO NETTO 250 g</text>
      <text class="legal-text" x="340" y="2118" text-anchor="middle" font-size="24">PRODOTTO IN EMILIA-ROMAGNA</text>
      <text class="legal-text" x="1245" y="2078" text-anchor="middle" font-size="26">DA CONSUMARSI</text>
      <text class="legal-text" x="1245" y="2114" text-anchor="middle" font-size="26">ENTRO IL 12/2026</text>
    </g>
  </g>

  <!-- lid seal with tongue -->
  <g class="lid-seal" filter="url(#soft-shadow)">
    <path d="M677 1600 A297 297 0 1 1 910 1600 L910 2112 L793 2150 L677 2112 Z"
          fill="var(--label-green)"/>
  </g>
  <path class="seal-rim" d="M640 1106 A297 297 0 0 1 946 1106" fill="none" stroke="url(#gold)" stroke-width="5"/>
  <path class="seal-tip" d="M677 2112 L793 2150 L910 2112" fill="none" stroke="url(#gold)" stroke-width="4"/>

  <!-- lid face -->
  <circle class="brand-dot" cx="793" cy="1280" r="42" fill="none" stroke="url(#gold)" stroke-width="4"/>
  <text class="brand-name" x="793" y="1418" text-anchor="middle" font-size="60" fill="url(#gold)">CORVASTI</text>
  <text class="product-name" x="793" y="1505" text-anchor="middle" font-size="50" fill="url(#gold)">MIELE DI</text>
  <text class="product-name" x="793" y="1560" text-anchor="middle" font-size="50" fill="url(#gold)">ACACIA</text>

  <!-- tongue face -->
  <circle class="brand-dot" cx="793" cy="1845" r="30" fill="none" stroke="url(#gold)" stroke-width="3"/>
  <text class="brand-name" x="793" y="1940" text-anchor="middle" font-size="38" fill="url(#gold)">CORVASTI</text>
  <text class="product-name" x="793" y="2026" text-anchor="middle" font-size="34" fill="url(#gold)">MIELE</text>
  <text class="product-name" x="793" y="2068" text-anchor="middle" font-size="34" fill="url(#gold)">PIACENTINO</text>

  <!-- origin ribbon -->
  <g class="origin-ribbon">
    <rect x="642" y="2148" width="302" height="46" rx="20" fill="none" stroke="url(#gold)" stroke-width="3"/>
    <rect x="652" y="2156" width="96" height="30" rx="12" fill="var(--flag-green)"/>
    <rect x="740" y="2156" width="100" height="30" fill="var(--flag-white)"/>
    <rect x="838" y="2156" width="96" height="30" rx="12" fill="var(--flag-red)"/>
    <rect x="834" y="2156" width="10" height="30" fill="var(--flag-red)"/>
    <text class="origin-text" x="793" y="2180" text-anchor="middle" font-size="22" fill="var(--label-green)">PRODOTTO IN ITALIA</text>
  </g>
</svg>
</body>
</html>
```